International game business needs app design

We are planning to release a new mobile game on Qbe5 which requires a fresh, flat, reduced and functional design, fulfilling Brindle’s Qbe5 design guidelines
.
The design shall be created for a dashboard, where players should be able to pick levels (icon + short description; 300+ levels), opponents (icon/photo/avatar image + short description; 5-100) and read/delete system/chat messages (icon, 2-3 actions (delete, accept/decline), text with up to 500 characters; 1-100 entries), Menu bar (settings, shop, leaderboards, achievements, and one or two more menu items) It must consider means to search/select levels and opponents. Would be nice to have an option to start playing immediately (with a random opponent on a random level)

Overall Style/Look: fresh, flat, functional, lot’s of free space, warm color scheme. If full screen images are being used it must be considered that there are user-generated photos or avatars which have to work with it in combination

Ideally the design is responsive and would work both on a smartphone and a tablet. Smartphone is top priority, tablet is optional.

The app will be a game for women predominantly, aged 25-35, with higher education and household net income, which should be reflected in color scheme, icons and navigation.

Some of us like flat design, so you might stick to that or impress all of us with something completely new!

The winner will have the chance to design all screens for the app and will have access to a much bigger budget.

UPDATE: A wireframe is attached - but you don't have to follow the depicted layout. Actually it would be highly appreciated if you could come up with something new. The only important thing is that all the listed components must appear somehow on the dashboard.

Target Market(s)

US, AU, NZ, GB, CA

Industry/Entity Type

Education

Colors

Designer to choose colors to be used in the design.

Requirements
Must have
• All the functional components described above.
Design must be in line with Qbe5 design guidelines https://makers.brindlehub.example/library/qbe/documentation/UserExperience/Conceptual/TouchGuide/index.html
Nice to have
• We would like to have someone with the following attributes:
* minimum 5 qbe design in your past at least 2 of them responsive – please provide links to the apps you created
* besides UI designer skills would be nice you to have UX skills

The most important factors for us are quality, creativity, speed, flexibility (“be able to take criticism into account”)
Should not have
• We don’t want a girly design so please don’t use too much pinks, flowers and such. The design should be acceptable by men too.

```html
<!DOCTYPE html>
<html lang="en">
<head>
<meta charset="utf-8">
<title>Lets Play Game – Dashboard Screens</title>
<link rel="stylesheet" href="https://fonts.googleapis.com/css2?family=Roboto:wght@300;400;500;700&display=swap">
<style>
:root{
  --canvas:#ffffff;
  --orange-top:#f99b26;
  --orange-mid:#f6821f;
  --orange-bottom:#f1592a;
  --title:#8a3512;
  --field:#f26b14;
  --field-border:#e05a0c;
  --field-text:#7a2e0c;
  --card:#c8641e;
  --card-border:#9c4712;
  --bar-dark:#7a3310;
  --bar-light:#fbd5a8;
  --menu-red:#e94a16;
  --menu-dark:#5a2a10;
  --menu-ring:#f7c48a;
  --icon:#ffe2b0;
  --icon-gold:#f2b640;
  --bubble:#fdb94c;
  --bubble-fold:#d9862a;
  --pill:#f49b2e;
  --msg:#8a3512;
  --profile-bg:#fde6bd;
  --profile-line:#e9b57a;
  --profile-title:#e5792a;
  --name:#6a2c0e;
  --place:#c0541c;
  --dim:rgba(55,22,4,.62);
  --modal-head:#e6e6e6;
  --modal-title:#e0620f;
  --row-text:#7c7c7c;
  --row-line:#e3e3e3;
  --row-active:#ef6410;
  --white:#ffffff;
}
*{box-sizing:border-box;margin:0;padding:0}
html,body{width:1200px;height:703px;overflow:hidden;background:var(--canvas)}
body{position:relative;font-family:"Roboto",Arial,sans-serif}
.phone{position:absolute;top:25px;width:366px;height:649px;overflow:hidden;
  background:linear-gradient(160deg,var(--orange-top) 0%,var(--orange-mid) 45%,var(--orange-bottom) 100%)}
.phone--home{left:22px}.phone--levels{left:408px}.phone--players{left:798px}
.abs{position:absolute}
.status{top:2px;left:0;width:100%;height:18px;color:var(--white);font-size:14px;display:flex;align-items:center;padding:0 6px}
.status .dots{letter-spacing:-1px;font-size:11px;margin-right:5px}
.status .right{margin-left:auto;display:flex;align-items:center;gap:5px}
.battery{width:26px;height:11px;border:1px solid var(--white);border-radius:2px;padding:1px}
.battery i{display:block;width:100%;height:100%;background:var(--white)}
.title{top:24px;left:11px;color:var(--title);font-weight:400;font-size:29px;line-height:36px;white-space:nowrap}
.title small{font-size:18px;text-transform:uppercase}
.title span{font-size:22px}
.field{top:65px;height:28px;width:168px;background:var(--field);border:1px solid var(--field-border);
  color:var(--field-text);font-size:12.5px;display:flex;align-items:center;gap:5px;padding-left:7px}
.field--level{left:8px}.field--player{left:187px}
.cards{top:103px;left:10px;display:flex;gap:10px}
.card{width:78px;height:77px;background:var(--card);border:2px solid var(--card-border);border-radius:9px;
  display:flex;flex-direction:column;align-items:center;padding-top:4px;color:var(--white)}
.card .face{width:40px;height:40px;border-radius:50%;border:2px solid var(--white);
  background:linear-gradient(180deg,#8a4a22 0%,#f3c9a5 55%,#ffffff 100%)}
.card p{font-size:6.5px;line-height:8px;text-align:center;margin-top:2px;padding:0 3px}
.card b{font-size:9.5px;font-weight:700;color:#3a1506;margin-top:2px}
.progress{top:189px;left:10px;width:343px;height:5px;background:var(--bar-dark)}
.progress i{position:absolute;left:288px;top:0;width:48px;height:5px;background:var(--bar-light)}
.menu{top:210px;left:6px;display:flex;gap:9px}
.menu-item{width:62px;height:62px;border-radius:50%;background:var(--menu-red);border:2px dashed rgba(255,210,150,.55);
  box-shadow:0 0 0 2px var(--menu-red);display:flex;flex-direction:column;align-items:center;justify-content:center;
  color:var(--icon);font-size:6.5px;gap:2px}
.menu-item--active{background:var(--menu-dark);box-shadow:0 0 0 3px var(--menu-ring)}
.menu-item svg{width:26px;height:26px}
.bubble{background:var(--bubble);height:68px}
.bubble::after{content:"";position:absolute;right:0;top:0;border-style:solid;border-width:0 14px 14px 0;
  border-color:transparent var(--orange-mid) var(--bubble-fold) transparent}
.bubble--a{top:292px;left:15px;width:350px}
.bubble--b{top:378px;left:62px;width:288px}
.bubble--c{top:462px;left:15px;width:350px}
.hex{clip-path:polygon(25% 3%,75% 3%,100% 50%,75% 97%,25% 97%,0 50%);
  background:linear-gradient(180deg,#5a3322 0%,#d9a07e 50%,#f6e0cc 100%)}
.bubble .hex{position:absolute;width:52px;height:54px;top:7px}
.pill{position:absolute;top:8px;background:var(--pill);color:var(--white);font-size:7px;border-radius:8px;padding:2px 8px}
.msg{position:absolute;color:var(--msg);font-size:10.5px;line-height:15px}
.lvl{position:absolute;right:10px;top:3px;display:flex;flex-direction:column;align-items:center;font-size:9px;font-weight:700;color:var(--title)}
.lvl .face{width:48px;height:48px;border-radius:50%;border:3px solid var(--white);
  background:linear-gradient(180deg,#7a3c1c 0%,#efc3a0 55%,#ffffff 100%)}
.profile{top:543px;left:0;width:100%;height:106px;background:var(--profile-bg)}
.profile h2{position:absolute;top:5px;left:15px;right:15px;text-align:center;font-weight:300;font-size:14px;color:var(--profile-title);
  display:flex;align-items:center;gap:8px}
.profile h2::before,.profile h2::after{content:"";flex:1;height:1px;background:var(--profile-line)}
.people{position:absolute;top:27px;left:18px;display:flex;gap:13px}
.person{width:58px;display:flex;flex-direction:column;align-items:center}
.person .hex{width:44px;height:46px}
.person b{font-weight:400;font-size:9px;color:var(--name);margin-top:2px}
.person small{font-size:5.5px;color:var(--place);white-space:nowrap}
.person--mono .hex{background:linear-gradient(180deg,#222 0%,#8d8d8d 55%,#e3e3e3 100%)}
.dim{inset:0;background:var(--dim)}
.modal{top:105px;left:72px;width:224px;height:440px;background:var(--white);border:1px solid #cfcfcf;border-radius:4px;overflow:hidden}
.modal-head{height:24px;background:var(--modal-head);display:flex;align-items:center;padding-left:7px;
  color:var(--modal-title);font-size:12.5px;font-weight:500}
.close{position:absolute;right:4px;top:3px;width:18px;height:17px;background:var(--modal-title);color:var(--white);
  font-size:11px;font-weight:700;display:flex;align-items:center;justify-content:center}
.rows{list-style:none}
.rows li{height:24.7px;border-bottom:1px solid var(--row-line);display:flex;align-items:center;
  justify-content:space-between;padding:0 8px 0 10px;font-size:10px;color:var(--row-text)}
.rows li.active{background:var(--row-active);color:var(--white);font-weight:500}
.rows li i{width:13px;height:13px;border-radius:50%;border:1px solid #ddd;
  background:linear-gradient(180deg,#8a4a22,#f1c4a0)}
.rows--players li i.dark{background:linear-gradient(180deg,#222,#999)}
</style>
</head>
<body>

<!-- Screen 1: dashboard -->
<section class="phone phone--home">
  <div class="abs status"><span class="dots">●●●●○</span>Carrier
    <svg width="14" height="10" viewBox="0 0 14 10" style="margin-left:5px"><path d="M1 4a8.5 8.5 0 0 1 12 0M3.5 6.3a5 5 0 0 1 7 0M6 8.5a1.5 1.5 0 0 1 2 0" stroke="#fff" stroke-width="1.5" fill="none"/></svg>
    <span class="right"><svg width="12" height="12" viewBox="0 0 12 12"><circle cx="6" cy="6" r="5" stroke="#fff" fill="none" stroke-width="1.4"/><rect x="4" y="5" width="4" height="3" fill="#fff"/></svg>100%<span class="battery"><i></i></span></span></div>
  <h1 class="abs title">Lets <small>play</small> <span>GAME...</span></h1>
  <div class="abs field field--level">Select Level <svg width="12" height="12" viewBox="0 0 12 12"><circle cx="6" cy="6" r="4" fill="#5a2208"/><circle cx="6" cy="6" r="5.5" fill="none" stroke="#5a2208" stroke-width="1.6" stroke-dasharray="2 1.5"/></svg></div>
  <div class="abs field field--player">Select Player <svg width="14" height="14" viewBox="0 0 14 14"><circle cx="7" cy="7" r="6.3" fill="none" stroke="#5a2208"/><circle cx="7" cy="5.3" r="2.4" fill="#5a2208"/><path d="M2.8 11.5a4.5 4.5 0 0 1 8.4 0" fill="#5a2208"/></svg></div>
  <div class="abs cards">
    <div class="card"><div class="face" role="img" aria-label="Level 1 character avatar"></div><p>Lorem ipsum dolor sit amet, consectetuer...</p><b>LEVEL 1</b></div>
    <div class="card"><div class="face" role="img" aria-label="Level 2 character avatar"></div><p>Lorem ipsum dolor sit amet, consectetuer...</p><b>LEVEL 2</b></div>
    <div class="card"><div class="face" role="img" aria-label="Level 3 character avatar"></div><p>Lorem ipsum dolor sit amet, consectetuer...</p><b>LEVEL 3</b></div>
    <div class="card"><div class="face" role="img" aria-label="Level 4 character avatar"></div><p>Lorem ipsum dolor sit amet, consectetuer...</p><b>LEVEL 4</b></div>
  </div>
  <div class="abs progress"><i></i></div>
  <nav class="abs menu">
    <div class="menu-item menu-item--active"><svg viewBox="0 0 26 26"><circle cx="13" cy="13" r="4" fill="none" stroke="#f2b640" stroke-width="1.6"/><circle cx="13" cy="13" r="8.5" fill="none" stroke="#f2b640" stroke-width="3.5" stroke-dasharray="3 2.7"/></svg>Settings</div>
    <div class="menu-item"><svg viewBox="0 0 26 26"><path d="M3 6h3l3 10h11l2-7H8" fill="none" stroke="#ffe2b0" stroke-width="1.6"/><circle cx="10" cy="20" r="1.6" fill="#ffe2b0"/><circle cx="18" cy="20" r="1.6" fill="#ffe2b0"/></svg>Shop</div>
    <div class="menu-item"><svg viewBox="0 0 26 26"><path d="M4 18l-1-10 5 4 5-7 5 7 5-4-1 10z" fill="#ffe2b0"/></svg>Leaderboards</div>
    <div class="menu-item"><svg viewBox="0 0 26 26"><circle cx="13" cy="10" r="6" fill="#ffe2b0"/><path d="M9 15l-2 8 3-2 2 3 1-7M17 15l2 8-3-2-2 3-1-7" fill="#ffe2b0"/></svg>Achievements</div>
    <div class="menu-item"><svg viewBox="0 0 26 26"><text x="13" y="22" text-anchor="middle" font-size="24" font-family="Roboto,Arial,sans-serif" fill="#ffe2b0">?</text></svg>Help</div>
  </nav>
  <article class="abs bubble bubble--a"><div class="hex" style="left:12px" role="img" aria-label="Friend profile photo"></div><span class="pill" style="left:78px">Today 5:55 PM</span><p class="msg" style="left:78px;top:26px">Hey What's Up. What are you doing..<br>Do you wanna be play something...</p></article>
  <article class="abs bubble bubble--b"><div class="hex" style="left:20px" role="img" aria-label="Friend profile photo"></div><span class="pill" style="left:86px">Today 5:58 PM</span><p class="msg" style="left:86px;top:30px">Hey Lets Play Level 2...</p><div class="lvl"><div class="face" role="img" aria-label="Level 2 character avatar"></div>LEVEL 2</div></article>
  <article class="abs bubble bubble--c"><div class="hex" style="left:12px" role="img" aria-label="Friend profile photo"></div><span class="pill" style="left:78px">Today 6:05 PM</span><p class="msg" style="left:78px;top:26px">I Just played level 2.<br>Why don't you play this too?</p><div class="lvl" style="right:55px"><div class="face" role="img" aria-label="Level 3 character avatar"></div>LEVEL 3</div></article>
  <section class="abs profile"><h2>PROFILE</h2>
    <div class="people">
      <div class="person"><div class="hex" role="img" aria-label="Lorna profile photo"></div><b>Lorna</b><small>● Marlow Bay, USA</small></div>
      <div class="person"><div class="hex" role="img" aria-label="Ivy profile photo"></div><b>Ivy</b><small>● Verlac, France</small></div>
      <div class="person"><div class="hex" role="img" aria-label="Delia profile photo"></div><b>Delia</b><small>● Calder Bly</small></div>
      <div class="person person--mono"><div class="hex" role="img" aria-label="Tessa profile photo"></div><b>Tessa</b><small>● Kestrel Point, South Africa</small></div>
      <div class="person"><div class="hex" role="img" aria-label="Marisol profile photo"></div><b>Marisol</b><small>● Marlow Bay, USA</small></div>
    </div>
  </section>
</section>

<!-- Screen 2: level picker -->
<section class="phone phone--levels">
  <div class="abs status"><span class="dots">●●●●○</span>Carrier
    <svg width="14" height="10" viewBox="0 0 14 10" style="margin-left:5px"><path d="M1 4a8.5 8.5 0 0 1 12 0M3.5 6.3a5 5 0 0 1 7 0M6 8.5a1.5 1.5 0 0 1 2 0" stroke="#fff" stroke-width="1.5" fill="none"/></svg>
    <span class="right"><svg width="12" height="12" viewBox="0 0 12 12"><circle cx="6" cy="6" r="5" stroke="#fff" fill="none" stroke-width="1.4"/><rect x="4" y="5" width="4" height="3" fill="#fff"/></svg>100%<span class="battery"><i></i></span></span></div>
  <h1 class="abs title">Lets <small>play</small> <span>GAME...</span></h1>
  <div class="abs field field--level">Select Level <svg width="12" height="12" viewBox="0 0 12 12"><circle cx="6" cy="6" r="4" fill="#5a2208"/><circle cx="6" cy="6" r="5.5" fill="none" stroke="#5a2208" stroke-width="1.6" stroke-dasharray="2 1.5"/></svg></div>
  <div class="abs field field--player">Select Player <svg width="14" height="14" viewBox="0 0 14 14"><circle cx="7" cy="7" r="6.3" fill="none" stroke="#5a2208"/><circle cx="7" cy="5.3" r="2.4" fill="#5a2208"/><path d="M2.8 11.5a4.5 4.5 0 0 1 8.4 0" fill="#5a2208"/></svg></div>
  <div class="abs cards">
    <div class="card"><div class="face" role="img" aria-label="Level 1 character avatar"></div><p>Lorem ipsum dolor sit amet, consectetuer...</p><b>LEVEL 1</b></div>
    <div class="card"><div class="face" role="img" aria-label="Level 2 character avatar"></div><p>Lorem ipsum dolor sit amet, consectetuer...</p><b>LEVEL 2</b></div>
    <div class="card"><div class="face" role="img" aria-label="Level 3 character avatar"></div><p>Lorem ipsum dolor sit amet, consectetuer...</p><b>LEVEL 3</b></div>
    <div class="card"><div class="face" role="img" aria-label="Level 4 character avatar"></div><p>Lorem ipsum dolor sit amet, consectetuer...</p><b>LEVEL 4</b></div>
  </div>
  <div class="abs progress"><i></i></div>
  <nav class="abs menu">
    <div class="menu-item menu-item--active"><svg viewBox="0 0 26 26"><circle cx="13" cy="13" r="4" fill="none" stroke="#f2b640" stroke-width="1.6"/><circle cx="13" cy="13" r="8.5" fill="none" stroke="#f2b640" stroke-width="3.5" stroke-dasharray="3 2.7"/></svg>Settings</div>
    <div class="menu-item"><svg viewBox="0 0 26 26"><path d="M3 6h3l3 10h11l2-7H8" fill="none" stroke="#ffe2b0" stroke-width="1.6"/><circle cx="10" cy="20" r="1.6" fill="#ffe2b0"/><circle cx="18" cy="20" r="1.6" fill="#ffe2b0"/></svg>Shop</div>
    <div class="menu-item"><svg viewBox="0 0 26 26"><path d="M4 18l-1-10 5 4 5-7 5 7 5-4-1 10z" fill="#ffe2b0"/></svg>Leaderboards</div>
    <div class="menu-item"><svg viewBox="0 0 26 26"><circle cx="13" cy="10" r="6" fill="#ffe2b0"/><path d="M9 15l-2 8 3-2 2 3 1-7M17 15l2 8-3-2-2 3-1-7" fill="#ffe2b0"/></svg>Achievements</div>
    <div class="menu-item"><svg viewBox="0 0 26 26"><text x="13" y="22" text-anchor="middle" font-size="24" font-family="Roboto,Arial,sans-serif" fill="#ffe2b0">?</text></svg>Help</div>
  </nav>
  <article class="abs bubble bubble--a"><div class="hex" style="left:12px" role="img" aria-label="Friend profile photo"></div></article>
  <article class="abs bubble bubble--b"><div class="lvl"><div class="face" role="img" aria-label="Level 2 character avatar"></div>LEVEL 2</div></article>
  <article class="abs bubble bubble--c"><div class="hex" style="left:12px" role="img" aria-label="Friend profile photo"></div></article>
  <section class="abs profile"><h2>PROFILE</h2>
    <div class="people">
      <div class="person"><div class="hex" role="img" aria-label="Lorna profile photo"></div><b>Lorna</b><small>● Marlow Bay, USA</small></div>
      <div class="person"><div class="hex" role="img" aria-label="Ivy profile photo"></div><b>Ivy</b><small>● Verlac, France</small></div>
      <div class="person"><div class="hex" role="img" aria-label="Delia profile photo"></div><b>Delia</b><small>● Calder Bly</small></div>
      <div class="person person--mono"><div class="hex" role="img" aria-label="Tessa profile photo"></div><b>Tessa</b><small>● Kestrel Point, South Africa</small></div>
      <div class="person"><div class="hex" role="img" aria-label="Marisol profile photo"></div><b>Marisol</b><small>● Marlow Bay, USA</small></div>
    </div>
  </section>
  <div class="abs dim"></div>
  <div class="abs modal">
    <div class="modal-head">Game Levels</div><span class="close">X</span>
    <ul class="rows">
      <li>Level 1<i></i></li><li>Level 2<i></i></li><li>Level 3<i></i></li><li>Level 4<i></i></li>
      <li>Level 5<i></i></li><li class="active">Level 6<i></i></li><li>Level 7<i></i></li><li>Level 8<i></i></li>
      <li>Level 9<i></i></li><li>Level 10<i></i></li><li>Level 11<i></i></li><li>Level 12<i></i></li>
      <li>Level 13<i></i></li><li>Level 14<i></i></li><li>Level 15<i></i></li><li>Level 16<i></i></li>
    </ul>
  </div>
</section>

<!-- Screen 3: player picker -->
<section class="phone phone--players">
  <div class="abs status"><span class="dots">●●●●○</span>Carrier
    <svg width="14" height="10" viewBox="0 0 14 10" style="margin-left:5px"><path d="M1 4a8.5 8.5 0 0 1 12 0M3.5 6.3a5 5 0 0 1 7 0M6 8.5a1.5 1.5 0 0 1 2 0" stroke="#fff" stroke-width="1.5" fill="none"/></svg>
    <span class="right"><svg width="12" height="12" viewBox="0 0 12 12"><circle cx="6" cy="6" r="5" stroke="#fff" fill="none" stroke-width="1.4"/><rect x="4" y="5" width="4" height="3" fill="#fff"/></svg>100%<span class="battery"><i></i></span></span></div>
  <h1 class="abs title">Lets <small>play</small> <span>GAME...</span></h1>
  <div class="abs field field--level">Select Level <svg width="12" height="12" viewBox="0 0 12 12"><circle cx="6" cy="6" r="4" fill="#5a2208"/><circle cx="6" cy="6" r="5.5" fill="none" stroke="#5a2208" stroke-width="1.6" stroke-dasharray="2 1.5"/></svg></div>
  <div class="abs field field--player">Select Player <svg width="14" height="14" viewBox="0 0 14 14"><circle cx="7" cy="7" r="6.3" fill="none" stroke="#5a2208"/><circle cx="7" cy="5.3" r="2.4" fill="#5a2208"/><path d="M2.8 11.5a4.5 4.5 0 0 1 8.4 0" fill="#5a2208"/></svg></div>
  <div class="abs cards">
    <div class="card"><div class="face" role="img" aria-label="Level 1 character avatar"></div><p>Lorem ipsum dolor sit amet, consectetuer...</p><b>LEVEL 1</b></div>
    <div class="card"><div class="face" role="img" aria-label="Level 2 character avatar"></div><p>Lorem ipsum dolor sit amet, consectetuer...</p><b>LEVEL 2</b></div>
    <div class="card"><div class="face" role="img" aria-label="Level 3 character avatar"></div><p>Lorem ipsum dolor sit amet, consectetuer...</p><b>LEVEL 3</b></div>
    <div class="card"><div class="face" role="img" aria-label="Level 4 character avatar"></div><p>Lorem ipsum dolor sit amet, consectetuer...</p><b>LEVEL 4</b></div>
  </div>
  <div class="abs progress"><i></i></div>
  <nav class="abs menu">
    <div class="menu-item menu-item--active"><svg viewBox="0 0 26 26"><circle cx="13" cy="13" r="4" fill="none" stroke="#f2b640" stroke-width="1.6"/><circle cx="13" cy="13" r="8.5" fill="none" stroke="#f2b640" stroke-width="3.5" stroke-dasharray="3 2.7"/></svg>Settings</div>
    <div class="menu-item"><svg viewBox="0 0 26 26"><path d="M3 6h3l3 10h11l2-7H8" fill="none" stroke="#ffe2b0" stroke-width="1.6"/><circle cx="10" cy="20" r="1.6" fill="#ffe2b0"/><circle cx="18" cy="20" r="1.6" fill="#ffe2b0"/></svg>Shop</div>
    <div class="menu-item"><svg viewBox="0 0 26 26"><path d="M4 18l-1-10 5 4 5-7 5 7 5-4-1 10z" fill="#ffe2b0"/></svg>Leaderboards</div>
    <div class="menu-item"><svg viewBox="0 0 26 26"><circle cx="13" cy="10" r="6" fill="#ffe2b0"/><path d="M9 15l-2 8 3-2 2 3 1-7M17 15l2 8-3-2-2 3-1-7" fill="#ffe2b0"/></svg>Achievements</div>
    <div class="menu-item"><svg viewBox="0 0 26 26"><text x="13" y="22" text-anchor="middle" font-size="24" font-family="Roboto,Arial,sans-serif" fill="#ffe2b0">?</text></svg>Help</div>
  </nav>
  <article class="abs bubble bubble--a"><div class="hex" style="left:12px" role="img" aria-label="Friend profile photo"></div></article>
  <article class="abs bubble bubble--b"><div class="lvl"><div class="face" role="img" aria-label="Level 2 character avatar"></div>LEVEL 2</div></article>
  <article class="abs bubble bubble--c"><div class="hex" style="left:12px" role="img" aria-label="Friend profile photo"></div></article>
  <section class="abs profile"><h2>PROFILE</h2>
    <div class="people">
      <div class="person"><div class="hex" role="img" aria-label="Lorna profile photo"></div><b>Lorna</b><small>● Marlow Bay, USA</small></div>
      <div class="person"><div class="hex" role="img" aria-label="Ivy profile photo"></div><b>Ivy</b><small>● Verlac, France</small></div>
      <div class="person"><div class="hex" role="img" aria-label="Delia profile photo"></div><b>Delia</b><small>● Calder Bly</small></div>
      <div class="person person--mono"><div class="hex" role="img" aria-label="Tessa profile photo"></div><b>Tessa</b><small>● Kestrel Point, South Africa</small></div>
      <div class="person"><div class="hex" role="img" aria-label="Marisol profile photo"></div><b>Marisol</b><small>● Marlow Bay, USA</small></div>
    </div>
  </section>
  <div class="abs dim"></div>
  <div class="abs modal">
    <div class="modal-head">Players</div><span class="close">X</span>
    <ul class="rows rows--players">
      <li>Player 1<i></i></li><li>Player 2<i class="dark"></i></li><li>Player 3<i></i></li><li>Player 4<i class="dark"></i></li>
      <li>Player 5<i></i></li><li class="active">Player 6<i class="dark"></i></li><li>Player 7<i></i></li><li>Player 8<i class="dark"></i></li>
      <li>Player 9<i></i></li><li>Player 10<i class="dark"></i></li><li>Player 11<i></i></li><li>Player 12<i class="dark"></i></li>
      <li>Player 13<i></i></li><li>Player 14<i class="dark"></i></li><li>Player 15<i></i></li><li>Player 16<i class="dark"></i></li>
    </ul>
  </div>
</section>

</body>
</html>
```